New Web Design Project- Maplebrook Elders

Maplebrook Elders is the Capital regions premiere, non-medical, in-home care & companionship service that unites "junior-senior" caregivers with "senior-senior" care recipients so that senior-seniors can remain safe & independent in their own homes.
Our compassionate "junior-senior" caregivers are all retirees that have already enjoyed rewarding careers and/or have raised families of their own and feel the need to pay-it-forward with their care for older seniors.
Services include grocery shopping, medical or dental appointments, errands, meal preparation & cleanup, light housekeeping, bed making, laundry, hobbies, reading, transportation, entertainment, games, mobility assistance/transfers, respite care, light yard work, pet walking.

Target Market(s)

Grown children of senior-seniors between who are between 55-70, predominantly the daughters (female). End users of services (senior-seniors) are typically 80-100 years old and living in own homes

Industry/Entity Type

Medical

Coding

Coded - Design and coding required

Number of Pages Required

5+ page

Font styles to use
Sans Serif

Colors
3277b5
ec1f27

Requirements
Must have
• supporting photos on each page. Contact us page. Promotional video (done) attached that doesn't take viewers off my site (https://vidshare.example/Kq7PzLm2Wx4).
• Also, need my downloadable brochure (attached).
• The following pages:
• Home. Services. About Us. News. Employment. Contact us. Junior-Seniors Assisting Senior-Seniors. Why non-medical in-home care. Who are junior-seniors?Financial effects of senior care. Do you need care? Does someone you love need care?
Should not have
• Any other photos or images other than what I've supplied.

```html
<!DOCTYPE html>
<html lang="en">
<head>
<meta charset="utf-8">
<title>Maplebrook Elders</title>
<link rel="stylesheet" href="https://fonts.googleapis.com/css2?family=Lato:wght@400;700&display=swap">
<style>
:root{
  --blue:#3277b5;
  --navy:#1f4f8a;
  --red:#ec1f27;
  --ink:#333;
  --muted:#666;
  --line:#ddd;
  --paper:#fff;
  --grey:#efefef;
}
*{box-sizing:border-box;margin:0;padding:0}
html,body{width:1200px;height:4615px;overflow:hidden}
body{font-family:'Lato',sans-serif;color:var(--ink);background:var(--paper);font-size:13px;line-height:1.55}
.wrap{width:1004px;margin:0 auto;position:relative}
/* header */
.site-header{height:68px;background:var(--paper);position:relative;z-index:2;box-shadow:0 1px 4px rgba(0,0,0,.1)}
.site-header .wrap{display:flex;align-items:center;justify-content:space-between;height:68px}
.brand{display:flex;align-items:center;gap:10px}
.brand-mark{width:34px;height:34px;background:var(--navy)}
.brand-name{font-size:24px;font-weight:700;color:var(--navy);line-height:1}
.brand-tag{display:block;font-size:10px;color:var(--muted);font-weight:400;margin-top:2px}
.main-nav{display:flex;gap:34px;font-size:14px;text-transform:uppercase}
.main-nav a{color:var(--ink);text-decoration:none;padding-bottom:6px}
.main-nav a.active{border-bottom:2px solid var(--red)}
/* hero */
.hero{height:486px;background:linear-gradient(120deg,#8a6a45 0%,#c9a57d 35%,#e6cdb0 55%,#b88660 80%,#6d5337 100%);position:relative}
.hero-band{position:absolute;top:347px;left:98px;width:1004px;height:71px;background:rgba(236,31,39,.88);color:#fff;font-size:38px;display:flex;align-items:center;justify-content:center}
/* contact strip */
.info-strip{height:98px;background:var(--paper)}
.info-box{position:absolute;top:0;left:0;width:1004px;height:98px;border:1px solid var(--line);display:flex;align-items:center;justify-content:space-around;font-size:15px}
.info-item{display:flex;align-items:center;gap:14px}
.info-item svg{width:26px;height:26px;fill:none;stroke:#777;stroke-width:1.6}
/* features */
.features{background:var(--grey);padding:80px 0 50px}
.feature{display:flex;height:215px;margin-bottom:44px;background:var(--paper);box-shadow:0 2px 6px rgba(0,0,0,.12)}
.feature.flip{flex-direction:row-reverse}
.feature-photo{width:342px;flex:none}
.feature-body{flex:1;padding:30px 50px}
.feature.flip .feature-body{text-align:right}
.feature-body h3{color:var(--red);font-size:15px;font-weight:400;margin-bottom:12px}
.feature-body p{font-size:13px;color:var(--muted);max-width:540px}
.feature.flip .feature-body p{margin-left:auto}
.btn{display:inline-block;background:var(--red);color:#fff;font-size:13px;padding:8px 0;width:170px;text-align:center;margin-top:18px}
/* services */
.services{height:410px;background:var(--paper);padding-top:48px}
.services .wrap{display:flex;gap:62px}
.video-box{width:302px;height:308px;background:linear-gradient(160deg,#3e6fae,#1f4f8a);flex:none;color:#fff;display:flex;flex-direction:column;align-items:center;justify-content:center;font-size:12px;text-align:center}
.video-box svg{width:78px;height:78px;margin-bottom:12px}
.services-list h2{font-size:34px;font-weight:400;margin-bottom:22px}
.service{display:flex;gap:16px;margin-bottom:22px}
.diamond{width:18px;height:18px;background:var(--red);transform:rotate(45deg);flex:none;margin-top:2px}
.service h4{color:var(--red);font-size:13px;text-transform:uppercase;font-weight:400}
.service p{color:var(--muted);max-width:600px;margin-top:10px}
/* testimonial */
.testimonial{height:431px;background:var(--grey);padding-top:42px;text-align:center}
.section-title{font-size:34px;font-weight:400}
.quote-box{margin:38px auto 0;width:948px;height:240px;border:3px solid #eaa5a8;position:relative;text-align:left;padding:45px 200px 0 30px;color:var(--muted)}
.quote-mark{font-size:56px;color:#bbb;line-height:1;position:absolute}
.portrait{position:absolute;right:-50px;top:-8px;width:200px;height:200px;border-radius:50%;border:6px solid var(--paper);box-shadow:0 0 0 3px #eaa5a8;background:radial-gradient(#9c8b7a,#4a4038)}
.author{position:absolute;left:80px;bottom:-30px;width:230px;height:52px;border:2px solid #eaa5a8;background:var(--grey);text-align:center;padding-top:6px;font-size:20px}
.author small{display:block;font-size:11px;color:var(--muted)}
/* news */
.news{height:533px;padding-top:48px;text-align:center}
.news-grid{display:flex;margin-top:32px;border-top:3px solid var(--red)}
.news-card{display:flex;width:502px;height:246px;text-align:left}
.news-photo{width:200px;flex:none}
.news-body{padding:36px 30px 0}
.news-body time{font-size:12px}
.news-body h4{font-size:14px;font-weight:700;margin:4px 0 24px}
.news-body p{color:var(--muted)}
.news .btn{margin-top:40px}
/* contact */
.contact{height:659px;background:var(--grey);padding-top:42px}
.contact .section-title{text-align:center}
.form-row{display:flex;justify-content:space-between;margin-top:38px}
.field{background:var(--paper);border:1px solid #ccc;height:47px;width:488px;padding:12px 14px;font-size:12px;color:#777}
.field.message{width:1004px;height:268px;margin-top:16px}
.contact .btn{display:block;margin:54px auto 0}
.cta-band{position:absolute;left:0;top:0;width:1004px;height:87px;background:var(--red);color:#fff;font-size:30px;display:flex;align-items:center;justify-content:center;border-radius:12px 12px 0 0}
.cta-wrap{height:0}
/* footer */
.site-footer{height:277px;background:var(--navy);color:#fff;margin-top:0}
.site-footer .wrap{display:flex;padding-top:26px}
.foot-col h5{font-size:15px;margin-bottom:18px}
.foot-address{width:400px;font-size:13px}
.foot-address p{margin-bottom:12px}
.foot-links{width:430px;list-style:none}
.foot-links li{font-size:12px;padding:6px 0;border-bottom:1px solid rgba(255,255,255,.2);width:220px}
.foot-links li::before{content:"› "}
.brochure{width:168px;height:225px;background:linear-gradient(#d8c8d8,#e7e2ea 55%,#2b5b98 56%);margin-left:auto}
.copyright{height:36px;background:#173e6e;color:#fff;font-size:11px;text-align:center;line-height:36px}
</style>
</head>
<body>
<header class="site-header">
  <div class="wrap">
    <div class="brand"><span class="brand-mark"></span><span class="brand-name">Maplebrook Elders<span class="brand-tag">Junior-Seniors assisting Senior-Seniors</span></span></div>
    <nav class="main-nav"><a class="active" href="#">Home</a><a href="#">Services</a><a href="#">About Us</a><a href="#">News</a><a href="#">Employment</a><a href="#">Contact Us</a></nav>
  </div>
</header>

<section class="hero" role="img" aria-label="Photo of a smiling senior woman with her caregiver outdoors">
  <div class="hero-band">The care and company you need to be at home</div>
</section>

<section class="info-strip">
  <div class="wrap">
    <div class="info-box">
      <div class="info-item"><svg viewBox="0 0 24 24"><path d="M3 11l9-7 9 7v9h-6v-6H9v6H3z"/></svg><span>P.O. Box 41, Brookfield Park,<br>New York 12000</span></div>
      <div class="info-item"><svg viewBox="0 0 24 24"><path d="M5 3h4l2 5-3 2a11 11 0 0 0 6 6l2-3 5 2v4a2 2 0 0 1-2 2A17 17 0 0 1 3 5a2 2 0 0 1 2-2z"/></svg><span>555 - 014 - 2290</span></div>
      <div class="info-item"><svg viewBox="0 0 24 24"><rect x="4" y="9" width="16" height="11"/><path d="M7 9V4h10v5M8 13h8M8 16h8"/></svg><span>555 - 014 - 3371</span></div>
      <div class="info-item"><svg viewBox="0 0 24 24"><circle cx="12" cy="8" r="4"/><path d="M4 21c1-5 5-7 8-7s7 2 8 7"/></svg><span>24h Support</span></div>
    </div>
  </div>
</section>

<section class="features">
  <div class="wrap">
    <article class="feature"><div class="feature-photo" role="img" aria-label="Photo of a caregiver helping a senior woman at home" style="background:linear-gradient(135deg,#6b5240,#c9a98a)"></div><div class="feature-body"><h3>Junior-Seniors Assisting Senior-Seniors</h3><p>Ipsum is simply dummy text of the printing and typesetting industry. Lorem Ipsum has been the industry's standard dummy text ever since the 1500s, when an unknown printer took a galley, but also the leap into.</p><span class="btn">Read More</span></div></article>
    <article class="feature flip"><div class="feature-photo" role="img" aria-label="Photo of two senior women talking on a sofa" style="background:linear-gradient(135deg,#9d8a9e,#e3d3d8)"></div><div class="feature-body"><h3>Why non-medical in-home care ?</h3><p>Ipsum is simply dummy text of the printing and typesetting industry. Lorem Ipsum has been the industry's standard dummy text ever since the 1500s, when an unknown printer took a galley, but also the leap into.</p><span class="btn">Read More</span></div></article>
    <article class="feature"><div class="feature-photo" role="img" aria-label="Photo of senior women playing a board game" style="background:linear-gradient(135deg,#8fa8a0,#e8ddc8)"></div><div class="feature-body"><h3>Who are junior-seniors?</h3><p>Ipsum is simply dummy text of the printing and typesetting industry. Lorem Ipsum has been the industry's standard dummy text ever since the 1500s, when an unknown printer took a galley, but also the leap into.</p><span class="btn">Read More</span></div></article>
    <article class="feature flip"><div class="feature-photo" role="img" aria-label="Photo of a senior couple reviewing finances on a laptop" style="background:linear-gradient(135deg,#5d4a3f,#bfb4a8)"></div><div class="feature-body"><h3>Financial effects of senior care</h3><p>Ipsum is simply dummy text of the printing and typesetting industry. Lorem Ipsum has been the industry's standard dummy text ever since the 1500s, when an unknown printer took a galley, but also the leap into.</p><span class="btn">Read More</span></div></article>
    <article class="feature"><div class="feature-photo" role="img" aria-label="Photo of a caregiver serving a meal to a senior man" style="background:linear-gradient(135deg,#8a4b38,#d6c4b0)"></div><div class="feature-body"><h3>Do you need care?</h3><p>Ipsum is simply dummy text of the printing and typesetting industry. Lorem Ipsum has been the industry's standard dummy text ever since the 1500s, when an unknown printer took a galley, but also the leap into.</p><span class="btn">Read More</span></div></article>
    <article class="feature flip"><div class="feature-photo" role="img" aria-label="Photo of a caregiver assisting a senior woman in her living room" style="background:linear-gradient(135deg,#2f4a5e,#8fa27a)"></div><div class="feature-body"><h3>Does someone you love need care?</h3><p>Ipsum is simply dummy text of the printing and typesetting industry. Lorem Ipsum has been the industry's standard dummy text ever since the 1500s, when an unknown printer took a galley, but also the leap into.</p><span class="btn">Read More</span></div></article>
  </div>
</section>

<section class="services">
  <div class="wrap">
    <a class="video-box" href="https://vidshare.example/Kq7PzLm2Wx4" style="text-decoration:none">
      <svg viewBox="0 0 80 80" fill="none" stroke="#fff" stroke-width="3"><circle cx="40" cy="40" r="36"/><path d="M32 26l22 14-22 14z" fill="#fff"/></svg>
      <span>Click Here to<br>Watch Our Video</span>
    </a>
    <div class="services-list">
      <h2>Our Services</h2>
      <div class="service"><span class="diamond"></span><div><h4>Grocery Shopping</h4><p>Lorem Ipsum is simply dummy text of the printing and typesetting industry. Lorem Ipsum has been the industry's standard dummy text ever since the 1500s, when an unknown printer took a galley, but also the leap into.</p></div></div>
      <div class="service"><span class="diamond"></span><h4>Medical or Dental Appointments</h4></div>
      <div class="service"><span class="diamond"></span><h4>Errands</h4></div>
      <div class="service"><span class="diamond"></span><h4>Meal Preparation &amp; Cleanup</h4></div>
    </div>
  </div>
</section>

<section class="testimonial">
  <h2 class="section-title">Testimonial</h2>
  <div class="quote-box">
    <span class="quote-mark" style="left:28px;top:10px">“</span>
    <p>Lorem Ipsum is simply dummy text of the printing and typesetting industry. Lorem Ipsum has been the industry's standard dummy text ever since the 1500s, when an unknown printer took a galley of type and scrambled it to make a type specimen book. It has survived not only five centuries, but also the leap into electronic typesetting, remaining essentially unchanged.</p>
    <span class="quote-mark" style="right:170px;top:130px">”</span>
    <div class="portrait" role="img" aria-label="Portrait photo of the client giving the testimonial"></div>
    <div class="author">John Doe<small>Lorem Ipsum</small></div>
  </div>
</section>

<section class="news">
  <h2 class="section-title">Recent News</h2>
  <div class="wrap">
    <div class="news-grid">
      <article class="news-card"><div class="news-photo" role="img" aria-label="Photo of a caregiver helping a senior with her coat" style="background:linear-gradient(135deg,#4f5f4a,#c8c0b0)"></div><div class="news-body"><time>February 22, 2016</time><h4>NEWS HEADING HERE</h4><p>Lorem Ipsum is simply dummy text of the printing and typesetting industry. Lorem Ipsum has been the industry's standard dummy.</p></div></article>
      <article class="news-card" style="border-top:3px solid var(--blue);margin-top:-3px"><div class="news-photo" role="img" aria-label="Photo of a senior woman at a hair salon" style="background:linear-gradient(135deg,#3a3030,#c4aa98)"></div><div class="news-body"><time>February 22, 2016</time><h4>NEWS HEADING HERE</h4><p>Lorem Ipsum is simply dummy text of the printing and typesetting industry. Lorem Ipsum has been the industry's standard dummy.</p></div></article>
    </div>
    <span class="btn">View More</span>
  </div>
</section>

<section class="contact">
  <h2 class="section-title">Contact Us</h2>
  <div class="wrap">
    <div class="form-row"><div class="field">Name</div><div class="field">Email</div></div>
    <div class="field message">Message</div>
    <span class="btn">Send</span>
  </div>
</section>

<div class="cta-wrap" style="position:relative;top:-87px"><div class="wrap"><div class="cta-band">The care and company you need to be at home Call 555-014-2290 today!</div></div></div>

<footer class="site-footer">
  <div class="wrap">
    <div class="foot-col foot-address">
      <h5>Address</h5>
      <p>Maplebrook Elders LLC</p>
      <p>P.O. Box 41, Brookfield Park,<br>New York 12000</p>
      <p>555 - 014 - 2290</p>
      <p>555 - 014 - 3371</p>
    </div>
    <div class="foot-col">
      <h5>Quick Links</h5>
      <ul class="foot-links"><li>HOME</li><li>SERVICES</li><li>ABOUT US</li><li>NEWS</li><li>EMPLOYMENT</li><li>CONTACT US</li></ul>
    </div>
    <div class="brochure" role="img" aria-label="Cover of the downloadable brochure"></div>
  </div>
</footer>
<div class="copyright">Copyright 2017. Maplebrook Elders LLC. All rights reserved</div>
</body>
</html>
```